A business selling natural soaps online and in farmers markets. I want it to reflect local commerce and natural lifestyle. My colors are olive green and saddle brown. I want the dimensions to be 2.25 x 3.25" with matte finish.
Updates

The name of my company is Fern Hollow Soapworks, LLC

Industry/Entity Type

Business

```html
<!DOCTYPE html>
<html lang="en">
<head>
<meta charset="utf-8">
<title>Fern Hollow Soapworks, LLC – Business Card</title>
<link href="https://fonts.googleapis.com/css2?family=PT+Sans:wght@400;700&display=swap" rel="stylesheet">
<style>
  :root {
    --olive: #6b7b22;
    --olive-dark: #4e5a16;
    --olive-light: #8c9c3e;
    --saddle: #8b4513;
    --saddle-dark: #6e3510;
    --paper: #ffffff;
    --ink: #1c1c1c;
    --backdrop: #eceae4;
  }
  * { box-sizing: border-box; margin: 0; padding: 0; }
  html, body {
    width: 1200px; height: 800px; overflow: hidden;
    background: var(--backdrop);
    font-family: "PT Sans", Arial, sans-serif;
  }
  .sheet {
    width: 1200px; height: 800px;
    display: flex; align-items: center; justify-content: center; gap: 40px;
  }
  .card {
    position: relative; width: 540px; height: 310px;
    box-shadow: 0 6px 18px rgba(0,0,0,.18);
    overflow: hidden;
  }
  .card--front {
    background: var(--olive);
    display: flex; align-items: center; justify-content: center;
  }
  .card--back { background: var(--paper); }

  .wordmark {
    display: flex; align-items: center; gap: 12px;
    font-weight: 400; white-space: nowrap;
  }
  .wordmark__dot { border-radius: 50%; flex: none; }
  .card--front .wordmark { color: var(--paper); font-size: 33px; }
  .card--front .wordmark__dot { width: 30px; height: 30px; background: var(--paper); }
  .card--back .wordmark {
    position: absolute; left: 28px; top: 36px;
    color: var(--olive); font-size: 26px;
  }
  .card--back .wordmark__dot { width: 24px; height: 24px; background: var(--saddle); }

  .holder { position: absolute; left: 28px; top: 126px; }
  .holder__name { color: var(--olive); font-size: 19px; font-weight: 400; }
  .holder__role { color: var(--ink); font-size: 11px; margin-top: 4px; margin-left: 14px; }

  .contacts {
    position: absolute; right: 30px; top: 124px;
    list-style: none; text-align: right;
  }
  .contacts li {
    display: flex; align-items: center; justify-content: flex-end; gap: 6px;
    color: var(--ink); font-size: 12px; line-height: 1; margin-bottom: 9px;
  }
  .contacts svg { width: 12px; height: 12px; flex: none; fill: var(--olive); }

  .swoosh { position: absolute; left: 0; bottom: 0; width: 540px; height: 310px; }
</style>
</head>
<body>
<main class="sheet">
  <section class="card card--front" aria-label="Card front">
    <div class="wordmark"><span class="wordmark__dot"></span><span>Fern Hollow Soapworks, LLC</span></div>
  </section>

  <section class="card card--back" aria-label="Card back">
    <svg class="swoosh" viewBox="0 0 540 310" aria-hidden="true">
      <path d="M0 200 C120 216 250 252 330 310 L0 310 Z" fill="var(--olive-light)"/>
      <path d="M0 215 C130 230 250 264 316 310 L0 310 Z" fill="var(--olive)"/>
      <path d="M0 230 C130 246 240 278 296 310 L0 310 Z" fill="var(--saddle)"/>
      <path d="M0 246 C120 260 220 288 266 310 L0 310 Z" fill="var(--olive-dark)"/>
      <path d="M0 264 C110 276 190 296 222 310 L0 310 Z" fill="var(--olive)"/>
      <path d="M330 310 C420 300 490 286 540 262 L540 310 Z" fill="var(--olive)"/>
      <path d="M360 310 C440 304 500 294 540 280 L540 310 Z" fill="var(--saddle-dark)"/>
    </svg>

    <div class="wordmark"><span class="wordmark__dot"></span><span>Fern Hollow Soapworks, LLC</span></div>

    <div class="holder">
      <p class="holder__name">Your Name</p>
      <p class="holder__role">Designation</p>
    </div>

    <ul class="contacts">
      <li>9874563210
        <svg viewBox="0 0 12 12"><path d="M3 0h6a1 1 0 0 1 1 1v10a1 1 0 0 1-1 1H3a1 1 0 0 1-1-1V1a1 1 0 0 1 1-1zm0 2v7h6V2z"/></svg></li>
      <li>044-111111
        <svg viewBox="0 0 12 12"><path d="M2.5 0.5l2 2.4-1.2 1.4c.7 1.6 2 2.9 3.6 3.6l1.4-1.2 2.4 2-1.3 2.3C4.8 10.6 1.4 7.2.3 2z"/></svg></li>
      <li>yourmail.145@fernhollow.com
        <svg viewBox="0 0 12 12"><path d="M0 2h12v8H0zm1 1l5 3.5L11 3z" fill-rule="evenodd"/></svg></li>
      <li>www.yoursite.com
        <svg viewBox="0 0 12 12"><path d="M6 0a6 6 0 1 0 0 12A6 6 0 0 0 6 0zm0 1c.8 0 1.6 2 1.7 4.5H4.3C4.4 3 5.2 1 6 1zM1.1 5.5A5 5 0 0 1 3.6 1.6c-.5 1-.8 2.4-.9 3.9zm0 1h1.6c.1 1.5.4 2.9.9 3.9a5 5 0 0 1-2.5-3.9zm3.2 0h3.4C7.6 9 6.8 11 6 11s-1.6-2-1.7-4.5zm5 0h1.6a5 5 0 0 1-2.5 3.9c.5-1 .8-2.4.9-3.9zm0-1c-.1-1.5-.4-2.9-.9-3.9a5 5 0 0 1 2.5 3.9z"/></svg></li>
      <li>your address
        <svg viewBox="0 0 12 12"><path d="M6 0a4 4 0 0 1 4 4c0 3-4 8-4 8S2 7 2 4a4 4 0 0 1 4-4zm0 2.5a1.5 1.5 0 1 0 0 3 1.5 1.5 0 0 0 0-3z"/></svg></li>
    </ul>
  </section>
</main>
</body>
</html>
```